“Be Part Of History! Great Web Design Needed For Local Business!”

Note: This is for design only. No coding required. We want to see your ideas for a great website! This will be a FUN design and not boring like others you may work on.

WE HAVE HAD ONLY 8 DESIGNERS SO FAR SUBMIT - THIS IS A WIDE OPEN CONTEST THAT COULD MAKE YOU GOOD MONEY. PLEASE CONSIDER JOINING!

Look we are needing a great website design for a local carpet cleaning business….I know you are asking how can you “be part of history” with a boring industry like carpet cleaning. Here is the deal….NO ONE in our city has a great design so when you are chosen as the designer you are literally making history by bringing a great design to our city in this industry…

I know it’s cheesy but I am trying to get you to use your skills to help us and make it fun at the same time.

Why work with us:

We are a professional company that has run hundreds of crowdsourced projects on multiple platforms. If you participate in this contest (we hope you do) you can expect great video feedback, consistent feedback, and also our guarantee that if we know your website design will not be what we are looking for we will notify you so you don’t waste your time if there is no chance of you winning.

We respect and recognize this is how you make your living and we will not play games. We look forward to an awesome contest and awesome website designs.

Design Brief:

For this project please let your creative ideas flow. We have given you a ton of info along with videos to help you understand what we are after, however we WANT your creativity to shine through in your designs!

We are looking for a fresh and fun new design for

http://www.brightloomfloors.example/

This is a local carpet cleaning company that does great work. Unfortunately the current web design is old, outdates, and looks like dirt. So how can they portray a great image with the site they currently have? They can’t so that is why we need your help.

This website needs to convey trust, professionalism, and be super clean and easy to navigate. People making decisions for carpet cleaners are doing this fast so we need to make the site stand out and easy to navigate.

As you can see the current site does not convey trust, looks amateur and does not make people believe that this business has been in business 20 years…this is actually the top company in Albuquerque, but the current site does not reflect that…

Here is a video to help explain what we like about the current site and what we don’t like:

http://clipvault.example/t/qWm4Rt8L

Here are some examples of other sites in their business that have some things we like:

http://www.fernwaycleaners.example/ Please watch video to learn what we like and don’t like:
http://clipvault.example/t/Zp3vHsLkWaQ

http://www.tidyharbor.example/ Please watch video to learn what we like and don’t like:
http://clipvault.example/t/jRw2TbXe

http://lorenvask.example/ Please watch video to learn what we like and don’t like:
http://clipvault.example/t/NdhuwqAy

http://willowbankcarpetcleaning.example/ Please watch video to learn what we like and don’t like:
http://clipvault.example/t/GTRP4XbmZ

NOTE: We do not want to copy anything outright. We want to learn, model and take their ideas and make them better. We also want to be flexible and take what we like along with your creativity to make an amazing design.

Here is what we are looking for in more specific terms:

Colors: We need to keep the teal/turquoise look of the site. But we need some contrasting colors. Also the client likes white “its clean” so we can use white space in this.

When looking at colors please know that the current site and look is NOT what we are going for. We are going for a clean and professional look but also a look that is BOLD, FUN, and Vibrant (hence the colors).

Menu: Horizontal. We like bold and easy to read menu items. Don’t make it small and cluttered.

Site Structure: Clean and easy to navigate. We have a lot of content to display so we need a clean structure that breaks up the text and content areas.

Images: Please pull images from the current site. We can always replace the images of course, but if you show them “their own stuff” in the new design you will be closer to winning because it will feel more like “them”

Look and Feel: Professional company, trusted, and makes people feel comfortable once they are there. We need to also convey clean and crisp. That is what people are looking for from them.

Content Areas: It is a safe bet that if it is on the current site we need it on the new site. So don’t drop anything as it makes it hard to “cut content”.

What we don't want: We do not want clutter, boring, or templates or themes. We don’t want too cartoony, too cute, or too fancy… Be creative!

WIREFRAME: http://clipvault.example/t/WsLoxPea

Out of respect to professional designers who really are working hard to win if you do not follow this brief, you submit worn out themes, templates, or boring designs you will be eliminated. We are offering great prize money for this so we expect great visual designs.

We look forward to seeing your great work! Please ask any question if you have them. We will be very responsive throughout this whole contest!

Hi all, I appreciate each of you for taking the time to submit designs. I have spend a considerable amount of time today creating feedback for each of you in written and video format. We are serious about this project and are looking forward to seeing new designs. Thank you! Dale

Hi all, First I want to thank all the designers. We have many good designs and at this point are working with our client to give feedback to all of you. If we gave you feedback them please complete our requests to be considered. If you submitted a design and have not received feedback it means your design is really good, and we are sharing with our clients to get feedback so we don't waste your time on unnecessary changes. Thanks for your patience and we will get back to you soon. Dale

Reason: Hi guys, Client was on vacation and is taking a bit more time to get us feedback. Thanks, Dale

Reason: Extending to allow designers to accommodate changes for us. Dale

Target Market(s)

Most of our clients are higher end affluent. On the residential side we mostly have females calling to book appointments for our service.

We also have large businesses like apartment complexes, office buildings etc calling for our services as well.

Industry/Entity Type

Business

Font styles to use
Sans Serif

Requirements
Must have
• Space for video
Horizontal Menu
Bold
Crisp and Clean
Nice to have
• Coupons, testimonials, services,
Should not have
• cluttered
vertical menu
template look

```html
<!DOCTYPE html>
<html lang="en">
<head>
<meta charset="utf-8">
<title>Brightloom Floors – Carpet &amp; Upholstery Cleaning</title>
<link rel="stylesheet" href="https://fonts.googleapis.com/css2?family=Open+Sans:wght@400;600;700&family=Raleway:wght@400;500&family=Lato:wght@300;700;900&family=Signika:wght@600&family=Covered+By+Your+Grace&display=swap">
<style>
:root{
  --green:#3aa43a;
  --green-dark:#24842a;
  --green-btn:#2f9a3a;
  --blue:#1c87cf;
  --blue-dark:#136fb0;
  --orange:#f7a233;
  --orange-light:#fdbf4e;
  --brown:#4a2a0c;
  --ink:#333;
  --text:#555;
  --muted:#888;
  --rule:#d6d6d6;
  --page:#ececec;
  --white:#fff;
  --footer:#333;
  --footer-base:#262626;
  --tile:#e7f4fc;
  --tile-border:#b9dcf2;
}
*{margin:0;padding:0;box-sizing:border-box}
html,body{width:855px;height:1200px;overflow:hidden}
body{position:relative;background:var(--page);font-family:"Open Sans",Arial,sans-serif;color:var(--text)}
.abs{position:absolute}

/* header */
.topline{left:0;top:0;width:855px;height:3px;background:var(--green)}
.header{left:0;top:3px;width:855px;height:69px;background:var(--white)}
.brand{left:152px;top:24px;display:flex;align-items:center;gap:8px}
.brand-mark{width:18px;height:18px;border-radius:50%;background:var(--green)}
.brand-name{font-family:"Open Sans",sans-serif;font-weight:700;font-size:19px;color:var(--green-dark);letter-spacing:.2px}
.quote-call{left:560px;top:22px;display:flex;align-items:center;gap:9px}
.quote-call .lead{font-size:9.5px;color:var(--ink);line-height:12px}
.quote-call .num{font-family:"Lato",sans-serif;font-size:17px;color:var(--green);line-height:20px}

/* nav */
.nav{left:0;top:72px;width:855px;height:26px;background:linear-gradient(var(--blue),var(--blue-dark))}
.nav ul{list-style:none;position:absolute;left:326px;top:0;display:flex;height:26px}
.nav li{font-family:"Open Sans",sans-serif;font-weight:600;font-size:9px;color:var(--white);height:26px;line-height:26px;padding:0 12px;border-right:1px solid rgba(255,255,255,.18)}
.nav li.active{background:linear-gradient(#47b347,var(--green-dark));padding:0 13px}

/* hero */
.hero{left:0;top:98px;width:855px;height:308px;background:linear-gradient(90deg,#5a6470 0%,#c9cdd2 30%,#9aa4ad 55%,#6b6560 80%,#a59c94 100%)}
.hero-band{left:125px;top:203px;width:730px;height:98px;background:rgba(40,40,40,.45)}
.hero-title{left:146px;top:212px;font-family:"Signika",sans-serif;font-weight:600;font-size:28.5px;line-height:36px;color:var(--white)}
.hero-arrow{top:222px}
.watch{left:506px;top:128px;font-family:"Covered By Your Grace",cursive;font-size:20px;color:var(--white)}
.video{left:466px;top:173px;width:243px;height:157px;background:var(--white);box-shadow:0 2px 8px rgba(0,0,0,.35)}
.video-still{position:absolute;left:44px;top:27px;width:155px;height:92px;background:linear-gradient(#eef6f6,#dcecec)}
.play{position:absolute;left:97px;top:44px}

/* call to action */
.cta{left:145px;top:377px;width:564px;height:69px;background:linear-gradient(#3eaf45,var(--green-dark))}
.cta-btn{position:absolute;left:17px;top:9px;width:258px;height:49px;border-radius:4px;background:linear-gradient(var(--orange-light),var(--orange));box-shadow:0 2px 2px rgba(0,0,0,.25);text-align:center;color:var(--brown)}
.cta-btn .small{font-size:11px;line-height:13px;padding-top:5px;display:block}
.cta-btn .big{font-family:"Lato",sans-serif;font-weight:900;font-size:25px;line-height:26px;display:block}
.cta-call{position:absolute;left:302px;top:20px;font-family:"Lato",sans-serif;font-weight:300;font-size:22px;color:var(--white);white-space:nowrap}
.cta-call b{font-weight:700}

/* content */
.content{left:145px;top:446px;width:564px;height:614px;background:var(--white)}
.section-title{font-family:"Raleway",sans-serif;font-size:17px;color:var(--ink)}
.rule{height:1px;background:var(--rule)}
.service-img{left:154px;width:167px;height:100px}
.service-name{left:335px;font-family:"Raleway",sans-serif;font-weight:500;font-size:12.5px;color:var(--ink)}
.service-copy{left:335px;width:214px;font-size:7.4px;line-height:10.2px;color:var(--text)}
.more{left:335px;width:56px;height:16px;border-radius:2px;background:linear-gradient(#43b34a,var(--green-btn));color:var(--white);font-size:7px;font-weight:600;text-align:center;line-height:16px}

.side-copy{left:564px;width:137px;font-size:7.4px;line-height:10px;color:var(--text)}
.avatar{left:565px;width:38px;height:38px;border:1px solid var(--rule);background:linear-gradient(#cfd6dd,#a9b3bc)}
.testi-copy{left:607px;width:95px;font-size:6.4px;line-height:8.4px;color:var(--text)}
.testi-by{left:565px;font-size:5.6px;color:var(--ink);white-space:nowrap}
.testi-by b{color:var(--blue-dark)}
.tile{left:564px;width:136px;border:1px solid var(--tile-border);background:var(--tile)}
.tile-art{position:absolute;left:6px;top:8px;width:36px;height:36px;background:linear-gradient(#7fc4ec,#4aa6dc);border-radius:3px}
.tile-label{position:absolute;left:49px;font-size:8.6px;line-height:10px;color:var(--ink);font-weight:600}
.offer{left:564px;top:954px;width:137px;height:90px;border:1px solid #c9c9c9;background:var(--white)}
.offer-art{position:absolute;right:0;top:0;width:58px;height:88px;background:linear-gradient(#f2f2f2,#d8e6f0)}
.offer .t1{position:absolute;left:5px;top:10px;font-weight:700;font-size:8.5px;color:#1f5f9c}
.offer .t2{position:absolute;left:5px;top:31px;font-weight:700;font-size:7.5px;color:#1f7bc0}
.offer .t3{position:absolute;left:5px;top:43px;font-weight:700;font-size:10px;color:#1f3f6c}
.offer .btn{position:absolute;left:3px;top:66px;width:61px;height:13px;background:#1f5f9c;color:var(--white);font-size:7.5px;font-weight:600;line-height:13px;padding-left:5px}

/* footer */
.footer{left:0;top:1060px;width:855px;height:105px;background:var(--footer)}
.footer-base{left:0;top:1165px;width:855px;height:35px;background:var(--footer-base)}
.foot-title{font-size:9px;font-weight:600;color:var(--white)}
.foot-list{list-style:none;font-size:6.8px;line-height:12.2px;color:#d8d8d8}
.foot-text{font-size:6.8px;line-height:12px;color:#d8d8d8}
.field{height:14px;background:var(--white);border-radius:2px;font-size:6px;color:var(--text);line-height:14px;padding-left:4px}
.submit{left:663px;top:1129px;width:37px;height:30px;background:var(--white);border-radius:2px;font-size:6.5px;color:var(--ink);text-align:center;line-height:30px}
.legal{font-size:6.6px;color:#aaa}
</style>
</head>
<body>

<div class="abs topline"></div>
<header class="abs header"></header>
<div class="abs brand"><span class="brand-mark"></span><span class="brand-name">BRIGHTLOOM FLOORS</span></div>
<div class="abs quote-call">
  <svg width="24" height="24" viewBox="0 0 24 24" aria-hidden="true"><circle cx="12" cy="12" r="11" fill="none" stroke="#3aa43a" stroke-width="1.3"/><path d="M9 7.5l1.6 2.4-1 1.1c.6 1.2 1.6 2.2 2.8 2.8l1.1-1 2.4 1.6-.7 1.6c-3.5-.2-6.8-3.5-7-7z" fill="#3aa43a"/></svg>
  <div><div class="lead">Get a quote Call Us today!</div><div class="num">000 - 123 - 4567</div></div>
</div>

<nav class="abs nav">
  <ul>
    <li class="active">HOME</li>
    <li>ABOUT US</li>
    <li>SERVICES</li>
    <li>CUSTOMER REVIEWS</li>
    <li>CONTACT US</li>
  </ul>
</nav>

<section class="abs hero" role="img" aria-label="Bright modern living room with white sofa, tall windows and a potted plant"></section>
<div class="abs hero-band"></div>
<h1 class="abs hero-title">We know the<br>meaning of cleaning</h1>
<svg class="abs hero-arrow" style="left:99px" width="24" height="40" viewBox="0 0 24 40" aria-hidden="true"><path d="M21 2L3 20l18 18" fill="none" stroke="#fff" stroke-width="2.5"/></svg>
<svg class="abs hero-arrow" style="left:735px" width="24" height="40" viewBox="0 0 24 40" aria-hidden="true"><path d="M3 2l18 18L3 38" fill="none" stroke="#fff" stroke-width="2.5"/></svg>
<div class="abs watch">Watch our video</div>
<svg class="abs" style="left:640px;top:140px" width="26" height="32" viewBox="0 0 26 32" aria-hidden="true"><path d="M2 3c12 0 18 8 18 24" fill="none" stroke="#fff" stroke-width="1.3"/><path d="M16 23l4 5 3-6" fill="none" stroke="#fff" stroke-width="1.3"/></svg>
<div class="abs video">
  <div class="video-still" role="img" aria-label="Video still showing the company name"></div>
  <svg class="play" width="56" height="56" viewBox="0 0 56 56" aria-label="Play video"><circle cx="28" cy="28" r="26" fill="#2b2b2b" stroke="#1f8fd6" stroke-width="3"/><path d="M23 19l14 9-14 9z" fill="#fff"/></svg>
</div>

<div class="abs cta">
  <div class="cta-btn"><span class="small">Click here to get a</span><span class="big">FREE QUOTE</span></div>
  <div class="cta-call">OR CALL <b>0400 555 019</b></div>
</div>

<main class="abs content"></main>

<h2 class="abs section-title" style="left:154px;top:460px">Our Services</h2>
<div class="abs rule" style="left:154px;top:490px;width:394px"></div>

<div class="abs service-img" style="top:503px;background:linear-gradient(#3fb04a 0%,#3fb04a 55%,#2a6fc4 100%)" role="img" aria-label="Vacuum cleaning a blue carpet"></div>
<h3 class="abs service-name" style="top:501px">Carpet and Upholstery Cleaning</h3>
<p class="abs service-copy" style="top:521px">Lorem ipsum dolor sit amet, consectetur adipisicing elit, sed do eiusmod tempor incididunt ut labore et dolore magna aliqua. Ut enim ad minim veniam, quis nostrud exercitation ullamco laboris nisi ut aliquip ex ea commodo consequat...</p>
<div class="abs more" style="top:577px">Read more</div>

<div class="abs service-img" style="top:614px;background:linear-gradient(135deg,#e6e2da,#b9b3a8)" role="img" aria-label="Cleaning tile and grout"></div>
<h3 class="abs service-name" style="top:611px">Tile and Grout Cleaning</h3>
<p class="abs service-copy" style="top:631px">Lorem ipsum dolor sit amet, consectetur adipisicing elit, sed do eiusmod tempor incididunt ut labore et dolore magna aliqua. Ut enim ad minim veniam, quis nostrud exercitation ullamco laboris nisi ut aliquip ex ea commodo consequat...</p>
<div class="abs more" style="top:688px">Read more</div>

<div class="abs service-img" style="top:724px;background:linear-gradient(135deg,#dfe3e6,#9aa3ab)" role="img" aria-label="Worker polishing a floor with a buffing machine"></div>
<h3 class="abs service-name" style="top:721px">Strip and Wax Floors</h3>
<p class="abs service-copy" style="top:741px">Lorem ipsum dolor sit amet, consectetur adipisicing elit, sed do eiusmod tempor incididunt ut labore et dolore magna aliqua. Ut enim ad minim veniam, quis nostrud exercitation ullamco laboris nisi ut aliquip ex ea commodo consequat...</p>
<div class="abs more" style="top:798px">Read more</div>

<div class="abs service-img" style="top:834px;background:linear-gradient(135deg,#6f7478,#2d3033)" role="img" aria-label="Vacuuming a car interior"></div>
<h3 class="abs service-name" style="top:831px">RVs and Cars</h3>
<p class="abs service-copy" style="top:851px">Lorem ipsum dolor sit amet, consectetur adipisicing elit, sed do eiusmod tempor incididunt ut labore et dolore magna aliqua. Ut enim ad minim veniam, quis nostrud exercitation ullamco laboris nisi ut aliquip ex ea commodo consequat...</p>
<div class="abs more" style="top:910px">Read more</div>

<div class="abs service-img" style="top:945px;background:linear-gradient(135deg,#e9e4dc,#c19a62)" role="img" aria-label="Man relaxing on a sofa with his dog"></div>
<h3 class="abs service-name" style="top:941px">Pets Urine Problems</h3>
<p class="abs service-copy" style="top:962px">Lorem ipsum dolor sit amet, consectetur adipisicing elit, sed do eiusmod tempor incididunt ut labore et dolore magna aliqua. Ut enim ad minim veniam, quis nostrud exercitation ullamco laboris nisi ut aliquip ex ea commodo consequat...</p>
<div class="abs more" style="top:1021px">Read more</div>

<h2 class="abs section-title" style="left:563px;top:460px">About Us</h2>
<div class="abs rule" style="left:563px;top:490px;width:138px"></div>
<p class="abs side-copy" style="top:501px">Lorem ipsum dolor sit amet, consectetur adipisicing elit, sed do eiusmod tempor incididunt ut labore et dolore magna aliqua.</p>
<p class="abs side-copy" style="top:550px">Ut enim ad minim veniam, quis nostrud exercitation ullamco laboris nisi ut aliquip ex ea commodo consequat. Duis aute irure dolor in reprehenderit in voluptate velit esse cillum dolore eu fugiat nulla pariatur. Excepteur sint occaecat cupidatat non proident, sunt in culpa qui officia deserunt mollit anim id est laborum.</p>

<h2 class="abs section-title" style="left:563px;top:649px">Testimonials</h2>
<div class="abs rule" style="left:563px;top:681px;width:138px"></div>

<div class="abs avatar" style="top:695px" role="img" aria-label="Customer portrait"></div>
<p class="abs testi-copy" style="top:694px">Lorem ipsum dolor sit amet, consectetur adipisicing elit, sed do eiusmod tempor incididunt ut labore et dolore magna aliqua.</p>
<div class="abs testi-by" style="top:741px"><b>Tomas Reiner</b> &nbsp; CEO, Designing &nbsp;|&nbsp; England</div>
<div class="abs rule" style="left:563px;top:753px;width:138px"></div>

<div class="abs avatar" style="top:762px" role="img" aria-label="Customer portrait"></div>
<p class="abs testi-copy" style="top:761px">Lorem ipsum dolor sit amet, consectetur adipisicing elit, sed do eiusmod tempor incididunt ut labore et dolore magna aliqua.</p>
<div class="abs testi-by" style="top:812px"><b>Tomas Reiner</b> &nbsp; CEO, Designing &nbsp;|&nbsp; England</div>
<div class="abs rule" style="left:563px;top:823px;width:138px"></div>

<div class="abs tile" style="top:832px;height:54px">
  <div class="tile-art" role="img" aria-label="Illustration of a domestic cleaner"></div>
  <div class="tile-label" style="top:18px">Domestic Cleaning<br>&amp; Home Help</div>
</div>
<div class="abs tile" style="top:891px;height:54px">
  <div class="tile-art" role="img" aria-label="Illustration of an office cleaner"></div>
  <div class="tile-label" style="top:18px">Office &amp; Commercial<br>Cleaning</div>
</div>

<div class="abs offer">
  <div class="offer-art" role="img" aria-label="Smiling cleaner holding a bucket of supplies"></div>
  <div class="t1">SPECIAL OFFERS</div>
  <div class="t2">CHECK OUT FOR</div>
  <div class="t3">SPECIAL OFFERS</div>
  <div class="btn">Click Here</div>
</div>

<footer class="abs footer"></footer>
<h4 class="abs foot-title" style="left:146px;top:1082px">Quick Links</h4>
<ul class="abs foot-list" style="left:146px;top:1098px"><li>Home</li><li>About</li><li>Services</li><li>Customer reviews</li><li>Contact</li></ul>
<h4 class="abs foot-title" style="left:267px;top:1082px">Our Services</h4>
<ul class="abs foot-list" style="left:267px;top:1098px"><li>Carpet &nbsp;Cleaning</li><li>Tile and Grout Cleaning</li><li>Strip and Wax Floors</li><li>RVs and Cars</li><li>Pet Urine Problems</li></ul>
<h4 class="abs foot-title" style="left:427px;top:1082px">Contact info</h4>
<svg class="abs" style="left:427px;top:1099px" width="7" height="9" viewBox="0 0 7 9" aria-hidden="true"><path d="M3.5 0A3.2 3.2 0 0 0 .3 3.2C.3 5.6 3.5 9 3.5 9s3.2-3.4 3.2-5.8A3.2 3.2 0 0 0 3.5 0zm0 4.4a1.2 1.2 0 1 1 0-2.4 1.2 1.2 0 0 1 0 2.4z" fill="#ddd"/></svg>
<p class="abs foot-text" style="left:440px;top:1098px">218 Larkspur Ave.<br>Fairhollow, NM, 87000<br>United States</p>
<svg class="abs" style="left:427px;top:1138px" width="8" height="8" viewBox="0 0 8 8" aria-hidden="true"><path d="M1.5 0l1.3 2-.8.9c.5 1 1.3 1.8 2.3 2.3l.9-.8 2 1.3-.6 1.3C3.7 6.8 1 4.1.8 1.3z" fill="#ddd"/></svg>
<p class="abs foot-text" style="left:440px;top:1136px">(505) 555-0142</p>
<svg class="abs" style="left:427px;top:1151px" width="8" height="6" viewBox="0 0 8 6" aria-hidden="true"><rect x=".4" y=".4" width="7.2" height="5.2" fill="none" stroke="#ddd" stroke-width=".8"/><path d="M.4.4L4 3.4 7.6.4" fill="none" stroke="#ddd" stroke-width=".8"/></svg>
<p class="abs foot-text" style="left:440px;top:1148px">info@brightloomfloors.example</p>
<h4 class="abs foot-title" style="left:564px;top:1082px">Newsletter</h4>
<p class="abs foot-text" style="left:564px;top:1098px;width:150px">Subscribe to our newsletter to get promotions and extra prices .</p>
<div class="abs field" style="left:564px;top:1129px;width:95px">Full Name:</div>
<div class="abs field" style="left:564px;top:1145px;width:95px">Email:</div>
<div class="abs submit">Sumbit</div>

<div class="abs footer-base"></div>
<p class="abs legal" style="left:146px;top:1177px">Copyright 2014. Brightloom Floors. &nbsp;All Rights Reserved.</p>
<p class="abs legal" style="left:621px;top:1177px">Terms of use | Privacy policy</p>

</body>
</html>
```